Vellmont Archive Systems Quillbase 720 Flyer

We have a requirement to start sending out product / service information to our clients and resellers. Currently this type of communication is only via the LinkedIn/ Twitter / Blog articles and we want to change this to an email campaign with pdf and the ability to print and send by post.

We have a powerpoint draft of the flyer that will be a pdf and potentially a handout but it looks like a powerpoint and not something classy. I have included the powerpoint and four images along with our current logo (although this may change soon)

Target Market(s)

MSP Resellers, Direct Clients

Industry/Entity Type

It Service

Colors

Designer to choose colors to be used in the design.

Requirements
Must have
• The flow and feel from our website and social media so that it has our identity. Our core colors are on the website. Anything new must be complementary.
• Modern and technical feel
Nice to have
• Sense of security and trust. Our new strap line is to be "Simple, Safe, Secure" so some experimentation on this would be nice
Should not have
• nothing of note

```html
<!DOCTYPE html>
<html lang="en">
<head>
<meta charset="utf-8">
<title>Vellmont Archive Systems – Understand the Risks</title>
<link rel="stylesheet" href="https://fonts.googleapis.com/css2?family=Montserrat:wght@400;500;700;800&display=swap">
<style>
  :root {
    --backdrop: #d9d9da;
    --panel-dark: #4b4e53;
    --panel-light: #8c9096;
    --blue-deep: #0d5fa3;
    --blue-soft: #4a8fc0;
    --white: #ffffff;
    --sand-light: #d9c7a8;
    --sand-mid: #c6a57d;
    --sky: #ebe6d6;
  }
  * { margin: 0; padding: 0; box-sizing: border-box; }
  html, body { width: 1200px; height: 833px; overflow: hidden; }
  body {
    background: var(--backdrop);
    font-family: "Montserrat", sans-serif;
    color: var(--white);
  }
  .spread {
    position: absolute;
    left: 20px; top: 16px;
    width: 1160px; height: 801px;
    overflow: hidden;
    box-shadow: 0 6px 24px rgba(0,0,0,0.18);
  }
  .spread-photo {
    position: absolute; inset: 0;
    background: linear-gradient(180deg, var(--sky) 0%, #ddd3bd 42%, var(--sand-light) 62%, var(--sand-mid) 100%);
  }
  .spread-shapes { position: absolute; inset: 0; }
  .spine {
    position: absolute; left: 579px; top: 0; width: 2px; height: 100%;
    background: linear-gradient(90deg, rgba(0,0,0,0.12), rgba(0,0,0,0));
  }
  .risks-title {
    position: absolute; left: 522px; top: 92px;
    font-size: 44px; font-weight: 800; letter-spacing: 1px;
    white-space: nowrap; line-height: 1.1;
  }
  .risks-column {
    position: absolute; left: 640px; top: 164px; width: 500px;
    display: flex; flex-direction: column;
  }
  .risks-copy {
    font-size: 12.5px; line-height: 1.45; font-weight: 400;
    text-align: justify;
  }
  .vulnerable-label {
    margin: 16px 0 14px -30px;
    width: 470px; height: 30px; padding-left: 30px;
    background: var(--blue-deep);
    font-size: 17px; font-weight: 700; line-height: 30px;
    white-space: nowrap;
  }
  .risk-list {
    list-style: none; font-size: 14px; font-weight: 700; line-height: 1.38;
    margin-bottom: 22px;
  }
  .risks-closing { margin-top: 12px; }
</style>
</head>
<body>
  <div class="spread">
    <div class="spread-photo" role="img" aria-label="Photo of a child in a helmet and goggles inside a toy cannon on a desert road, with sand extending under the text panel"></div>

    <svg class="spread-shapes" width="1160" height="801" viewBox="0 0 1160 801" aria-hidden="true">
      <path d="M500 0 H580 V801 H520 C505 600 500 300 500 0 Z" fill="var(--panel-light)"/>
      <path d="M500 0 H580 V70 C555 55 525 50 500 52 Z" fill="var(--blue-soft)"/>
      <path d="M580 0 H1160 V620 C980 635 780 660 580 695 Z" fill="var(--panel-dark)"/>
      <path d="M580 0 H1160 V70 C960 62 760 70 580 88 Z" fill="var(--blue-deep)"/>
    </svg>
    <div class="spine"></div>

    <h1 class="risks-title">UNDERSTAND THE RISKS</h1>

    <div class="risks-column">
      <p class="risks-copy">Northvale ensure that your applications and data are available to you but your Quillbase 720 data is still vulnerable to some significant risks. There are many studies that report about how data loss can be pretty devastating for a company but the time lost in attempting data recovery can be equally damaging.</p>

      <div class="vulnerable-label">Cloud-based data is vulnerable to:</div>

      <ul class="risk-list">
        <li>Malware damage and ransomware attacks</li>
        <li>Accidental or malicious deletion</li>
        <li>Retention policy gaps and confusion</li>
        <li>Cancelled user licenses causing data loss</li>
        <li>Intentional or accidental data overwrites</li>
        <li>Lost time when restoring data</li>
      </ul>

      <p class="risks-copy">Northvale does provide some restore abilities but they are very primitive and come with some pretty important limits that companies are unaware of. There is a study by Northvale that state that data compromises can go undetected for about 140 days but the Recycle Bin only keeps the data for 93 days.</p>

      <p class="risks-copy risks-closing">That by itself should be a good enough reason to consider a backup service to protect your business.</p>
    </div>
  </div>
</body>
</html>
```